New Business Card Design Project

Use the flyer uploaded and website www.brightoakbuilders.com for inspiration.
List Our Services on Backside of business cards
Martin Hollis
Harborline Renovations Inc.
Licensed General Contractors
858-471-9063

Contact Information for Business Card

Use the flyer uploaded and website www.brightoakbuilders.com for inspiration. List Our Services on Backside of business cards Martin Hollis Harborline Renovations Inc. Licensed General Contractors 858-471-9063

```html
<!DOCTYPE html>
<html lang="en">
<head>
<meta charset="utf-8">
<title>Harborline Renovations – Business Card</title>
<link rel="stylesheet" href="https://fonts.googleapis.com/css2?family=Marcellus&family=Roboto:wght@400;700&display=swap">
<style>
  :root {
    --backdrop: #3b3b3b;
    --card: #111111;
    --silver: #d6d6d6;
    --silver-soft: #a9a9a9;
  }
  html, body {
    margin: 0;
    width: 1200px;
    height: 801px;
    overflow: hidden;
    background: var(--backdrop);
  }
  .stage {
    position: relative;
    width: 1200px;
    height: 801px;
  }
  .card {
    position: absolute;
    top: 252px;
    width: 520px;
    height: 297px;
    background: var(--card);
    box-shadow: 0 10px 28px rgba(0,0,0,0.45);
    color: var(--silver);
  }
  .card--contact { left: 50px; }
  .card--brand { left: 630px; }

  .brand-mark {
    display: flex;
    align-items: center;
    gap: 10px;
    font-family: "Marcellus", serif;
    font-weight: 400;
    color: var(--silver);
    letter-spacing: 0.06em;
    text-transform: uppercase;
    white-space: nowrap;
  }
  .brand-mark__square {
    border: 1.5px solid var(--silver);
    flex: none;
  }
  .card--contact .brand-mark {
    position: absolute;
    left: 24px;
    top: 132px;
    font-size: 15px;
  }
  .card--contact .brand-mark__square { width: 12px; height: 12px; }
  .card--brand .brand-mark {
    position: absolute;
    left: 0;
    right: 0;
    top: 128px;
    justify-content: center;
    font-size: 24px;
  }
  .card--brand .brand-mark__square { width: 18px; height: 18px; }

  .divider {
    position: absolute;
    left: 262px;
    top: 70px;
    width: 1px;
    height: 150px;
    background: var(--silver-soft);
  }
  .contact {
    position: absolute;
    left: 284px;
    top: 72px;
    font-family: "Roboto", sans-serif;
  }
  .contact__name {
    margin: 0;
    font-size: 17px;
    font-weight: 700;
    letter-spacing: 0.02em;
    color: #f0f0f0;
    text-transform: uppercase;
  }
  .contact__title,
  .contact__company {
    margin: 4px 0 0;
    font-size: 13px;
    font-weight: 400;
  }
  .contact__company { margin-top: 14px; }
  .contact__list {
    list-style: none;
    padding: 0;
    margin: 22px 0 0;
    font-size: 13px;
  }
  .contact__item {
    display: flex;
    align-items: center;
    gap: 8px;
    margin-bottom: 8px;
  }
  .contact__icon { width: 12px; height: 12px; flex: none; }
</style>
</head>
<body>
<main class="stage">

  <section class="card card--contact" aria-label="Business card front">
    <div class="brand-mark">
      <span class="brand-mark__square"></span>
      <span>Harborline Renovations</span>
    </div>
    <div class="divider"></div>
    <div class="contact">
      <h1 class="contact__name">Martin Hollis</h1>
      <p class="contact__title">Licensed General Contractors</p>
      <p class="contact__company">Harborline Renovations Inc.</p>
      <ul class="contact__list">
        <li class="contact__item">
          <svg class="contact__icon" viewBox="0 0 12 12" aria-hidden="true">
            <circle cx="6" cy="6" r="6" fill="#d6d6d6"/>
            <path d="M4 3.2c.4-.3.8-.2 1 .2l.5 1c.1.3 0 .6-.2.8l-.3.3c.3.7.8 1.2 1.5 1.5l.3-.3c.2-.2.5-.3.8-.2l1 .5c.4.2.5.6.2 1l-.4.4c-.5.5-1.4.4-2.6-.4C5 7.3 4.3 6.3 3.8 5.4 3.3 4.5 3.3 3.8 3.6 3.5z" fill="#111"/>
          </svg>
          <span>858-471-9063</span>
        </li>
        <li class="contact__item">
          <svg class="contact__icon" viewBox="0 0 12 12" aria-hidden="true">
            <circle cx="6" cy="6" r="6" fill="#d6d6d6"/>
            <circle cx="6" cy="6" r="3.6" fill="none" stroke="#111" stroke-width="0.8"/>
            <path d="M2.4 6h7.2M6 2.4c-1.3 1.8-1.3 5.4 0 7.2M6 2.4c1.3 1.8 1.3 5.4 0 7.2" fill="none" stroke="#111" stroke-width="0.7"/>
          </svg>
          <span>www.brightoakbuilders.com</span>
        </li>
      </ul>
    </div>
  </section>

  <section class="card card--brand" aria-label="Business card back">
    <div class="brand-mark">
      <span class="brand-mark__square"></span>
      <span>Harborline Renovations</span>
    </div>
  </section>

</main>
</body>
</html>
```